A new type of air filter for interior of vehicles

HI
I have included a file to show the basics of what i want and all the information that should be needed ,i now need this to be "designed" and to be created for a information flyer first and as things progress web pages etc etc look forward to the designs

Industry/Entity Type

Interior

Contact Information for Business Card

probably the same "theme type" as the brochure which will carry through to Business card and on to online marketing in the future

Font styles to use
Serif
Sans Serif

```html
<!DOCTYPE html>
<html lang="en">
<head>
<meta charset="utf-8">
<title>Clearpath Air Filters – Business Card Concepts</title>
<link rel="stylesheet" href="https://fonts.googleapis.com/css2?family=Archivo:wdth,wght@62..125,400..800&display=swap">
<style>
  :root {
    --sheet: #000000;
    --card-light: #ffffff;
    --card-grey: #808080;
    --ink: #000000;
    --ink-reverse: #ffffff;
    --accent: #3fa9f5;
  }
  * { margin: 0; padding: 0; box-sizing: border-box; }
  html, body {
    width: 1200px; height: 1115px; overflow: hidden;
    background: var(--sheet);
    font-family: "Archivo", Arial, sans-serif;
    font-stretch: 125%;
  }
  .sheet { position: relative; width: 1200px; height: 1115px; }

  .card { position: absolute; width: 543px; height: 314px; background: var(--card-light); color: var(--ink); }
  .card--front { left: 39px; }
  .card--back { left: 619px; }
  .card--grey { background: var(--card-grey); }
  .row-1 { top: 78px; }
  .row-2 { top: 409px; }
  .row-3 { top: 758px; height: 310px; }

  /* brand lockup on the fronts */
  .brand { position: absolute; display: flex; align-items: center; gap: 18px; }
  .brand__dot { width: 64px; height: 64px; border-radius: 50%; background: var(--ink); flex: none; }
  .brand__name { font-weight: 800; font-size: 30px; line-height: 1; letter-spacing: -0.5px; text-transform: uppercase; }
  .row-1 .brand { left: 120px; top: 118px; }
  .row-2 .brand { left: 120px; top: 118px; }
  .row-3 .brand { left: 60px; top: 104px; }
  .brand--reverse .brand__name { color: var(--ink-reverse); line-height: 1.05; }

  /* backs */
  .title { position: absolute; left: 34px; font-weight: 800; text-transform: uppercase; line-height: 1; letter-spacing: -0.5px; }
  .title__accent { color: var(--accent); }
  .contact { position: absolute; font-size: 12.5px; line-height: 16px; font-weight: 400; }

  .back-1__rule { position: absolute; left: 19px; top: 112px; width: 3px; height: 141px; background: var(--ink); }
  .back-1__title { top: 114px; font-size: 27px; }
  .back-1__contact { left: 34px; top: 148px; }

  .back-2__title { top: 88px; font-size: 32px; line-height: 1; }
  .back-2__rule { position: absolute; left: 34px; top: 160px; width: 302px; height: 3px; background: var(--ink); }
  .back-2__contact { left: 34px; top: 182px; }
  .back-2__post { left: 346px; top: 182px; }

  .back-3__title { top: 60px; font-size: 42px; line-height: 1; }
  .back-3__rule { position: absolute; left: 34px; top: 152px; width: 408px; height: 5px; background: var(--ink); }
  .back-3__contact { left: 34px; top: 176px; }
  .back-3__post { left: 346px; top: 176px; }
</style>
</head>
<body>
<main class="sheet">

  <section class="card card--front row-1">
    <div class="brand">
      <span class="brand__dot"></span>
      <span class="brand__name">Clearpath</span>
    </div>
  </section>

  <section class="card card--back row-1">
    <span class="back-1__rule"></span>
    <h2 class="title back-1__title">Clearpath Air Filters</h2>
    <p class="contact back-1__contact">
      0400-555-019<br>
      hello@clearpathair.com<br>
      ClearpathAirFilters.com.au<br>
      Po Box 12<br>
      Harbour Point Qld<br>
      4000
    </p>
  </section>

  <section class="card card--front row-2">
    <div class="brand">
      <span class="brand__dot"></span>
      <span class="brand__name">Clearpath</span>
    </div>
  </section>

  <section class="card card--back row-2">
    <h2 class="title back-2__title">Clearpath Air<br>Filters</h2>
    <span class="back-2__rule"></span>
    <p class="contact back-2__contact">
      0400-555-019<br>
      hello@clearpathair.com<br>
      ClearpathAirFilters.com.au
    </p>
    <p class="contact back-2__post">
      Po Box 12<br>
      Harbour Point Qld<br>
      4000
    </p>
  </section>

  <section class="card card--front card--grey row-3">
    <div class="brand brand--reverse">
      <span class="brand__name">Clearpath<br>Air<br>Filters</span>
      <span class="brand__dot"></span>
    </div>
  </section>

  <section class="card card--back card--grey row-3">
    <h2 class="title back-3__title">Clearpath <span class="title__accent">Air</span><br>Filters</h2>
    <span class="back-3__rule"></span>
    <p class="contact back-3__contact">
      0400-555-019<br>
      hello@clearpathair.com<br>
      ClearpathAirFilters.com.au
    </p>
    <p class="contact back-3__post">
      Po Box 12<br>
      Harbour Point Qld<br>
      4000
    </p>
  </section>

</main>
</body>
</html>
```